J & M Holloway Carpet & Gutter Cleaning

We clean carpets and have an environmentally friendly gutter machine that cleans out the guttering leaving no mess
Phone 0427816350
or 0438261907

Industry/Entity Type

Business

```html
<!DOCTYPE html>
<html lang="en">
<head>
<meta charset="utf-8">
<title>J &amp; M Holloway Carpet &amp; Gutter Cleaning</title>
<link rel="stylesheet" href="https://fonts.googleapis.com/css2?family=Cinzel:wght@500;700&display=swap">
<style>
  :root {
    --bg-center: #ffffff;
    --bg-mid: #b4c7d3;
    --bg-edge: #7f9cb0;
    --brand-blue: #1c69a6;
    --gutter-green: #00a651;
    --carpet-red: #ed1c24;
    --handset: #1a1a1a;
  }
  html, body {
    margin: 0;
    padding: 0;
    overflow: hidden;
    background: var(--bg-edge);
  }
  .card {
    position: relative;
    width: 1200px;
    height: 791px;
    overflow: hidden;
    background: radial-gradient(ellipse 62% 62% at 50% 58%, var(--bg-center) 0%, var(--bg-mid) 45%, var(--bg-edge) 100%);
    font-family: "Cinzel", serif;
    color: var(--brand-blue);
  }
  .service-badge {
    position: absolute;
    top: 97px;
    width: 188px;
    height: 188px;
    border-radius: 50%;
  }
  .service-badge--gutter { left: 385px; background: var(--gutter-green); }
  .service-badge--carpet { left: 630px; background: var(--carpet-red); }
  .business-name {
    position: absolute;
    top: 318px;
    left: 0;
    width: 100%;
    margin: 0;
    text-align: center;
    font-weight: 700;
    font-size: 72px;
    letter-spacing: 5px;
    line-height: 1;
  }
  .services {
    position: absolute;
    top: 420px;
    left: 0;
    width: 100%;
    margin: 0;
    text-align: center;
    font-weight: 500;
    font-size: 35px;
    letter-spacing: 5px;
    line-height: 1;
    text-transform: uppercase;
  }
  .contact {
    position: absolute;
    top: 555px;
    left: 355px;
    display: flex;
    align-items: center;
    gap: 38px;
  }
  .contact__icon { width: 96px; height: 122px; }
  .contact__numbers {
    display: flex;
    flex-direction: column;
    align-items: center;
    font-weight: 500;
    line-height: 1;
  }
  .contact__phone { font-size: 42px; letter-spacing: 3px; }
  .contact__or { font-size: 30px; letter-spacing: 3px; margin: 10px 0 8px; }
</style>
</head>
<body>
  <main class="card">
    <div class="service-badge service-badge--gutter" role="img" aria-label="Gutter cleaning icon: gutter and downpipe with a leaf"></div>
    <div class="service-badge service-badge--carpet" role="img" aria-label="Carpet cleaning icon: carpet cleaning wand"></div>

    <h1 class="business-name">J &amp; M Holloway</h1>
    <p class="services">Carpet &amp; Gutter Cleaning</p>

    <div class="contact">
      <svg class="contact__icon" viewBox="0 0 96 122" aria-hidden="true">
        <path fill="var(--handset)" d="M22 4 L38 2 Q44 2 44 8 L44 26 Q44 32 38 34 L30 37 Q26 40 28 48 L44 84 Q48 90 54 88 L62 84 Q68 82 72 88 L84 104 Q88 110 82 114 L70 120 Q58 124 46 114 Q26 96 12 62 Q0 32 8 14 Q12 6 22 4 Z"/>
      </svg>
      <div class="contact__numbers">
        <span class="contact__phone">042-781-6350</span>
        <span class="contact__or">or</span>
        <span class="contact__phone">043-826-1907</span>
      </div>
    </div>
  </main>
</body>
</html>
```